Business card for STEADYWAVE

Please design professional business card for IT consulting firm STEADYWAVE INC.
Use logo attached.
Use information from sample qNode business card attached.
replace qnode inc with STEADYWAVE INC.
as well as qnodeinc.com with steadywave.example

```html
<!DOCTYPE html>
<html lang="en">
<head>
<meta charset="utf-8">
<title>STEADYWAVE Business Card</title>
<link href="https://fonts.googleapis.com/css2?family=Montserrat:wght@400;500;700&display=swap" rel="stylesheet">
<style>
  :root {
    --backdrop: #5a5a5a;
    --card: #ffffff;
    --ink: #111111;
    --purple: #7b3fa0;
    --orange: #f39a1e;
    --teal: #4cc3b0;
    --sky: #3fb6e6;
    --wash-a: #e6f6f4;
    --wash-b: #efe6f5;
  }
  * { margin: 0; padding: 0; box-sizing: border-box; }
  html, body {
    width: 1200px; height: 900px; overflow: hidden;
    background: var(--backdrop);
    font-family: "Montserrat", Arial, sans-serif;
  }
  .card {
    position: absolute; left: 105px; top: 150px;
    width: 990px; height: 600px;
    background: var(--card);
    box-shadow: 0 12px 30px rgba(0,0,0,.35);
    overflow: hidden;
  }
  .card__wash {
    position: absolute; right: -40px; top: 90px;
    width: 330px; height: 330px;
    background: linear-gradient(160deg, var(--wash-a), var(--wash-b));
    opacity: .8;
  }
  .wordmark {
    position: absolute; left: 70px; top: 70px;
    display: flex; align-items: center; gap: 20px;
  }
  .wordmark__name {
    font-weight: 700; font-size: 92px; letter-spacing: 6px; color: var(--ink);
  }
  .wordmark__mark {
    width: 34px; height: 34px; background: var(--purple); align-self: flex-start; margin-top: 6px;
  }
  .person { position: absolute; left: 90px; top: 230px; }
  .person__name { font-weight: 700; font-size: 34px; color: var(--purple); letter-spacing: 1px; }
  .person__title { font-weight: 500; font-size: 24px; color: var(--ink); letter-spacing: 1px; margin-top: 2px; }
  .rule { position: absolute; left: 90px; top: 340px; width: 60px; height: 3px; background: var(--orange); }
  .contacts {
    position: absolute; left: 90px; top: 370px;
    display: grid; grid-template-columns: auto auto; column-gap: 48px; row-gap: 10px;
    font-size: 23px; color: var(--ink);
  }
  .contact { display: flex; align-items: center; gap: 12px; }
  .contact svg { width: 20px; height: 20px; flex: none; }
  .company { position: absolute; left: 90px; top: 470px; font-size: 23px; color: var(--ink); line-height: 1.3; }
  .company__name { font-weight: 700; color: var(--purple); }
</style>
</head>
<body>
  <div class="card">
    <div class="card__wash" aria-hidden="true"></div>

    <div class="wordmark">
      <span class="wordmark__name">STEADYWAVE</span>
      <span class="wordmark__mark" aria-hidden="true"></span>
    </div>

    <div class="person">
      <div class="person__name">ANTON BELKORSKY</div>
      <div class="person__title">GENERAL MANAGER</div>
    </div>

    <div class="rule"></div>

    <div class="contacts">
      <div class="contact">
        <svg viewBox="0 0 20 20"><path d="M5 2l3 4-2 2c1 2 3 4 5 5l2-2 4 3-2 3C9 17 3 11 2 4z" fill="var(--purple)"/></svg>
        (555) 214-3080 ext.201
      </div>
      <div class="contact">
        <svg viewBox="0 0 20 20"><path d="M5 2l3 4-2 2c1 2 3 4 5 5l2-2 4 3-2 3C9 17 3 11 2 4z" fill="var(--teal)"/></svg>
        (555) 630-2194
      </div>
      <div class="contact">
        <svg viewBox="0 0 20 20"><rect x="2" y="5" width="16" height="11" fill="var(--sky)"/><path d="M2 5l8 6 8-6" fill="none" stroke="#fff" stroke-width="1.5"/></svg>
        abelkorsky@steadywave.example
      </div>
      <div class="contact">
        <svg viewBox="0 0 20 20"><circle cx="10" cy="10" r="8" fill="var(--orange)"/><path d="M2 10h16M10 2c-3 3-3 13 0 16M10 2c3 3 3 13 0 16" fill="none" stroke="#fff" stroke-width="1.2"/></svg>
        www.steadywave.example
      </div>
    </div>

    <div class="company">
      <div class="company__name">STEADYWAVE INC.</div>
      <div>1280 Harbourline Rd, Suite 101</div>
      <div>Brookfield, Ontario, A1B 2C3, Canada</div>
    </div>
  </div>
</body>
</html>
```